Modern multimedia website for Tindall Legal

Website required for a Maritime Law practice in Australia - to modernise old existing one see www.tindalllegal-example.com

Requires resizable website suitable for web, desktop, Phone and Tablet viewing.

Site has to be uncluttered, clear, elegant and modern. Has to instil, confidence, knowledge, trust. An not appear like a stuffy conservative firm.

Logo already designed (attached).

Colours - any suitable to purpose and design.

Would like to display RSS feed(s) but not essential.

Would also like to have a blog component that links to ConnectaPro, Chirpwave, Snapframe, Orbitnet + (Accounts already exist).

Already have Domain registered - Need to be able to upload files easily

All Website passwords (uploading etc) to remain with Tindall Legal.

Have attached own images (with identification and trade mark images removed for possible use.)

No images or text to be used that is protected by others copy-write or trademark to be used.

Text for web site to be provided , can be suggested or modification of current website text - am flexible

Target Market(s)

Professional organisations - Shipowners, Operators, Global companies. Luxury Yacht owners,

Industry/Entity Type

Legal

Coding

Coded - Design and coding required

Number of Pages Required

1 page

Requirements
Must have
• Be easy for me to upload to domain server - i am not a computer person.
• Site to be modern style ( flexible with page number) but must be easy and quick to load .
Nice to have
• RSS Feed with feeds from : Harbour Ledger QXR, vBosun & Seaway -Bulletin.
Should not have
• Look like a conservative Law form.

```html
<!DOCTYPE html>
<html lang="en">
<head>
<meta charset="utf-8">
<title>Tindall Legal – Admiralty and Maritime Lawyers</title>
<link rel="stylesheet" href="https://fonts.googleapis.com/css2?family=Montserrat:wght@400;600;700&family=Open+Sans:wght@400;600&display=swap">
<style>
:root{
  --blue:#1570be;
  --blue-dark:#0e4f8f;
  --ink:#222;
  --muted:#777;
  --grey-band:#dcdcdc;
  --line:#d0d0d0;
  --footer:#1b1b1b;
  --footer-bar:#111;
  --white:#fff;
}
*{margin:0;padding:0;box-sizing:border-box}
html,body{width:1200px;height:2365px;overflow:hidden}
body{position:relative;font-family:"Open Sans",Arial,sans-serif;color:var(--ink);background:var(--white)}
.abs{position:absolute}
.btn{position:absolute;display:flex;align-items:center;justify-content:center;background:linear-gradient(#1d78c4,var(--blue-dark));color:var(--white);font-family:"Montserrat",Arial,sans-serif;font-size:12px;letter-spacing:.5px;border-radius:3px;box-shadow:0 2px 3px rgba(0,0,0,.25)}

/* hero */
.hero{left:0;top:0;width:1200px;height:567px;background:linear-gradient(180deg,#5d7fc2 0%,#7e9ad0 30%,#5a5f6c 55%,#2d3440 80%,#1d2530 100%)}
.nav-rule{position:absolute;height:1px;background:rgba(255,255,255,.35)}
.nav a{position:absolute;top:70px;color:var(--white);font-family:"Montserrat",Arial,sans-serif;font-size:15px;text-decoration:none;transform:translateX(-50%)}
.brand{position:absolute;left:600px;top:106px;transform:translateX(-50%);text-align:center;color:var(--white);font-family:"Open Sans",Arial,sans-serif}
.brand .name{font-size:30px;line-height:36px}
.brand .tag{font-size:15px;line-height:19px}
.hero h1{position:absolute;left:0;width:1200px;top:278px;text-align:center;color:var(--white);font-family:"Montserrat",Arial,sans-serif;font-weight:700;font-size:37px;text-shadow:0 2px 4px rgba(0,0,0,.5)}
.hero h2{position:absolute;left:0;width:1200px;top:328px;text-align:center;color:var(--white);font-family:"Montserrat",Arial,sans-serif;font-weight:400;font-size:28px;text-shadow:0 2px 4px rgba(0,0,0,.5)}
.dots span{position:absolute;top:527px;width:17px;height:17px;border-radius:50%;background:#555}
.dots span.on{background:var(--white)}

/* about */
.about-photo{left:601px;top:567px;width:599px;height:370px;background:linear-gradient(135deg,#8a3b30 0%,#5a4a48 40%,#a0503c 65%,#4c6a8e 100%)}
.about h3{position:absolute;left:142px;top:628px;font-family:"Montserrat",Arial,sans-serif;font-weight:400;font-size:30px;color:#333}
.about p{position:absolute;left:142px;top:680px;width:420px;font-size:14.5px;line-height:27px;color:var(--muted)}

/* services */
.services{left:0;top:937px;width:1200px;height:378px;background:var(--blue);color:var(--white)}
.services h3{position:absolute;top:55px;width:1200px;text-align:center;font-family:"Montserrat",Arial,sans-serif;font-weight:400;font-size:24px;letter-spacing:.5px}
.services .lede{position:absolute;top:92px;width:1200px;text-align:center;font-family:"Montserrat",Arial,sans-serif;font-size:16px}
.svc-col{position:absolute;top:157px;list-style:none;font-family:"Montserrat",Arial,sans-serif;font-size:12.5px}
.svc-col li{height:28.3px;position:relative;padding-left:16px}
.svc-col li::before{content:"";position:absolute;left:0;top:4px;border-left:5px solid #bcd6ee;border-top:4px solid transparent;border-bottom:4px solid transparent}

/* feature cards */
.grey-band{left:0;top:1315px;width:1200px;height:353px;background:var(--grey-band)}
.card{position:absolute;background:var(--white);border:1px solid #c8c8c8}
.card h4{position:absolute;left:29px;top:20px;font-family:"Montserrat",Arial,sans-serif;font-weight:400;font-size:20px;color:#222}
.card .photo{position:absolute;left:28px;top:57px;width:196px;height:146px}
.card p{position:absolute;left:238px;top:58px;width:200px;font-size:11.5px;line-height:20px;color:#555}
.card .btn{left:240px;top:172px;width:99px;height:30px;font-size:11px}

/* news */
.news-card{position:absolute;top:1706px;height:309px;border:1px solid #c8c8c8;background:var(--white)}
.news-card h4{position:absolute;left:29px;top:20px;font-family:"Montserrat",Arial,sans-serif;font-weight:400;font-size:22px;color:#333}
.item{position:absolute;left:29px;width:400px}
.date{position:absolute;left:0;top:0;width:55px;height:60px;border:1px solid #ccc;text-align:center}
.date .d{height:40px;background:var(--blue);color:var(--white);font-size:23px;line-height:40px;font-family:"Montserrat",Arial,sans-serif}
.date .m{font-size:11px;line-height:18px;color:#666;background:#eee}
.thumb{position:absolute;left:0;top:0;width:69px;height:69px;border-radius:50%;background:linear-gradient(180deg,#8fb0d8,#43505e 60%,#7a4a3c)}
.item .t{position:absolute;left:74px;top:2px;font-family:"Montserrat",Arial,sans-serif;font-size:16px;color:var(--blue);white-space:nowrap}
.item .b{position:absolute;left:74px;top:27px;width:330px;font-size:11.5px;line-height:17px;color:#888}
.item .r{position:absolute;left:74px;top:64px;font-family:"Montserrat",Arial,sans-serif;font-size:12px;color:#111}
.more{position:absolute;left:36px;top:269px;font-family:"Montserrat",Arial,sans-serif;font-size:11.5px;color:#444;display:flex;align-items:center;gap:8px}
.more i{display:inline-block;width:19px;height:19px;border-radius:50%;background:#ddd;position:relative}
.more i::after{content:"";position:absolute;left:7px;top:5px;border-left:5px solid #777;border-top:4px solid transparent;border-bottom:4px solid transparent}

/* footer */
.footer{left:0;top:2079px;width:1200px;height:239px;background:var(--footer);color:var(--white)}
.footer .brand{top:123px;left:263px}
.footer .brand .name{font-size:28px}
.footer .brand .tag{font-size:14px}
.fcol{position:absolute;top:52px}
.fcol h5{font-family:"Montserrat",Arial,sans-serif;font-weight:400;font-size:17px;margin-bottom:8px}
.fcol li{list-style:none;font-size:12px;line-height:23.5px;display:flex;align-items:center;gap:6px}
.fcol svg{flex:none}
.social li{font-size:12px;line-height:22px}
.footer-bar{left:0;top:2318px;width:1200px;height:47px;background:var(--footer-bar);color:#888;font-size:11px;text-align:center;line-height:47px}
</style>
</head>
<body>

<header class="abs hero" role="img" aria-label="Photo of two luxury catamaran vessels moored at a marina under a blue sky">
  <div class="nav-rule" style="left:166px;top:58px;width:307px"></div>
  <div class="nav-rule" style="left:166px;top:103px;width:307px"></div>
  <div class="nav-rule" style="left:740px;top:58px;width:317px"></div>
  <div class="nav-rule" style="left:740px;top:103px;width:317px"></div>
  <nav class="nav">
    <a style="left:194px">HOME</a>
    <a style="left:305px">ABOUT US</a>
    <a style="left:429px">SERVICES</a>
    <a style="left:787px">NEWS</a>
    <a style="left:880px">BLOG</a>
    <a style="left:987px">CONTACT</a>
  </nav>
  <div class="brand">
    <div class="name">Tindall Legal</div>
    <div class="tag">Admiralty and Maritime<br>lawyers</div>
  </div>
  <h1>MARITIME LAW PRACTICE IN AUSTRALIA</h1>
  <h2>ETIAM SED PORTA SUSPENDISSE</h2>
  <a class="btn" style="left:530px;top:383px;width:132px;height:40px;font-size:13px">CONTACT US</a>
  <div class="dots">
    <span class="on" style="left:554px"></span>
    <span style="left:576px"></span>
    <span style="left:597px"></span>
    <span style="left:619px"></span>
  </div>
</header>

<section class="about">
  <h3>About Tindall Legal</h3>
  <p>Tindall Legal is a boutique law practice specializing in Admiralty and Maritime legal advice. Operating from a base in Queensland, Tindall Legal is able to advise clients in all Australian States and Territories on a wide range of Admiralty and Maritime legal matters.</p>
  <a class="btn" style="left:140px;top:833px;width:112px;height:34px">READ MORE</a>
  <div class="abs about-photo" role="img" aria-label="Photo of stacked steel pipes and cargo containers on a wharf"></div>
</section>

<section class="abs services">
  <h3>OUR SERVICES</h3>
  <div class="lede">We are able to assist by providing cost efficient and effective legal services in relation to</div>
  <ul class="svc-col" style="left:162px">
    <li>Australian domestic commercial vessels</li>
    <li>International shipping</li>
    <li>Limitation of liability matters</li>
    <li>Superyachts</li>
    <li>Australian coastal trading</li>
  </ul>
  <ul class="svc-col" style="left:467px">
    <li>Vessel sale and purchases</li>
    <li>Offshore oil and gas marine operations</li>
    <li>Pollution matters</li>
    <li>Casualty &amp; Emergency response</li>
    <li>Port or coastal tug operations</li>
  </ul>
  <ul class="svc-col" style="left:785px">
    <li>Cargo damage and disputes</li>
    <li>Australian maritime legislation compliance</li>
    <li>Maritime evidence gathering and analysis</li>
    <li>Charterparty amendment and disputes</li>
    <li>Admiralty Arrests</li>
  </ul>
</section>

<section class="abs grey-band">
  <article class="card" style="left:140px;top:51px;width:455px;height:230px">
    <h4>WHAT WE DO</h4>
    <div class="photo" role="img" aria-label="Photo of a crane loading containers at a port" style="background:linear-gradient(135deg,#7d98b0,#4a5660 55%,#8a5a40)"></div>
    <p>Commodo a mi Morbi ornare gravida elit Integer congue augue et malesuada iaculis ipsum dui aliquet felis at cursus magna nisl nec elit Praesent elementum elit</p>
    <a class="btn">READ MORE</a>
  </article>
  <article class="card" style="left:604px;top:51px;width:453px;height:230px">
    <h4>HOW WE WORK</h4>
    <div class="photo" role="img" aria-label="Photo of a fire-fighting vessel spraying water at sea" style="background:linear-gradient(180deg,#c9d3dc,#9aa7b2 50%,#7a4a34)"></div>
    <p>Commodo a mi Morbi ornare gravida elit Integer congue augue et malesuada iaculis ipsum dui aliquet felis at cursus magna nisl nec elit Praesent elementum elit</p>
    <a class="btn">READ MORE</a>
  </article>
</section>

<section>
  <article class="news-card" style="left:140px;width:451px">
    <h4>Harbour Ledger QXR News</h4>
    <div class="item" style="top:70px">
      <div class="date"><div class="d">05</div><div class="m">AUG</div></div>
      <div class="t">Maecenas at justo velit placerat</div>
      <div class="b">Ut nisi erat fermentum vel congue id euismod in elit Fusce ultricies orci ac feugiat suscipit leo</div>
      <div class="r">READ MORE</div>
    </div>
    <div class="item" style="top:173px">
      <div class="date"><div class="d">05</div><div class="m">AUG</div></div>
      <div class="t">Vivamus porttitor purus nisi</div>
      <div class="b">Ut nisi erat fermentum vel congue id euismod in elit Fusce ultricies orci ac feugiat suscipit leo</div>
      <div class="r">READ MORE</div>
    </div>
    <div class="more">VIEW MORE NEWS <i></i></div>
  </article>
  <article class="news-card" style="left:607px;width:451px">
    <h4>vBosun &amp; Maritime News</h4>
    <div class="item" style="top:68px">
      <div class="thumb" role="img" aria-label="Photo of a tug at sea"></div>
      <div class="t">Curabitur tristique mi condimentu</div>
      <div class="b">Ut nisi erat fermentum vel congue id euismod in elit Fusce ultricies orci ac feugiat suscipit leo</div>
      <div class="r">READ MORE</div>
    </div>
    <div class="item" style="top:171px">
      <div class="thumb" role="img" aria-label="Photo of a cargo ship deck"></div>
      <div class="t">Nullam enim leo egestas</div>
      <div class="b">Ut nisi erat fermentum vel congue id euismod in elit Fusce ultricies orci ac feugiat suscipit leo</div>
      <div class="r">READ MORE</div>
    </div>
    <div class="more">VIEW MORE NEWS <i></i></div>
  </article>
</section>

<footer class="abs footer">
  <div class="brand">
    <div class="name">Tindall Legal</div>
    <div class="tag">Admiralty and Maritime<br>lawyers</div>
  </div>
  <div class="fcol" style="left:400px">
    <h5>COMPANY</h5>
    <ul><li>Home</li><li>About Us</li><li>Our Services</li><li>Case Studies</li></ul>
  </div>
  <div class="fcol" style="left:531px">
    <h5>RESOURCES</h5>
    <ul><li>Team</li><li>Support</li><li>Blogs</li><li>Contact Us</li></ul>
  </div>
  <div class="fcol" style="left:678px">
    <h5>CONTACT US</h5>
    <ul>
      <li>Company Name</li>
      <li>18 Keelson Rd Harbourview QLD 4999</li>
      <li><svg width="12" height="12" viewBox="0 0 12 12"><path d="M2 1l2.5 0 1 3-1.5 1a7 7 0 0 0 3 3l1-1.5 3 1V11A10 10 0 0 1 1 2z" fill="none" stroke="#fff" stroke-width="1.2"/></svg>(07) 5550 1942</li>
      <li><svg width="12" height="10" viewBox="0 0 12 10"><rect x="0.5" y="0.5" width="11" height="9" fill="#fff"/><path d="M0.5 0.5L6 5l5.5-4.5" fill="none" stroke="#1b1b1b" stroke-width="1"/></svg>hello@tindalllegal-example.com</li>
    </ul>
  </div>
  <div class="fcol social" style="left:886px">
    <h5>FOLLOW US</h5>
    <ul><li>ConnectaPro</li><li>Chirpwave</li><li>Orbitnet +</li><li>Snapframe</li></ul>
  </div>
</footer>
<div class="abs footer-bar">© 2016 Company Name &nbsp;All right reserved</div>

</body>
</html>
```